Stonefield Partners Business Card Design

We are looking for a new business card design, we are not happy with our current design. We are a boutique management consulting firm and our clients are typically fortune 500 companies.

I have attached the current front and back that we have as well as a version of our logo that can be used. I am trying to get a higher resolution version of the logo file to upload to the project.

Target Market(s)

Fortune 500 companies are our primary client base. Financial services, life sciences, pharmaceuticals and telecom companies are

Industry/Entity Type

Management Consulting

Contact Information for Business Card

We are trying to communicate a high degree of professionalism, a somewhat minimalist perhaps with some air of whimsy (without overdoing it). Attached is the current design, front and back as well as logos. I like the current back of the card and assume we will keep the phrase the same.

From a color palette perspective, I prefer to stay with a gray scale as they are today.

Font styles to use
Sans Serif

Colors
1b1b1b
474747
ffffff

Requirements
Must have
• Two sided business card design. File format should be something that can be used outside of Photoshop like MS Publisher so that they can be edited with personal information.
• Font should be calibri or something very similar and should be available within MS Office
Should not have
• No other logos or graphics outside of the logo provided.

```html
<!DOCTYPE html>
<html lang="en">
<head>
<meta charset="utf-8">
<title>Stonefield Partners Business Card</title>
<link rel="stylesheet" href="https://fonts.googleapis.com/css2?family=Carlito:wght@400;700&family=Arimo:wght@400;700&family=Roboto:wght@400;500&display=swap">
<style>
  :root {
    --stage: #707070;
    --ink: #000000;
    --paper: #ffffff;
    --ink-soft: #1b1b1b;
    --mid: #474747;
  }
  * { margin: 0; padding: 0; box-sizing: border-box; }
  html, body { width: 1200px; height: 900px; overflow: hidden; }
  body { background: var(--stage); position: relative; font-family: "Carlito", "Calibri", sans-serif; }

  .card { position: absolute; width: 477px; height: 294px; overflow: hidden; }
  .card-front { left: 116px; top: 275px; background: var(--paper); color: var(--ink); }
  .card-back { left: 622px; top: 276px; background: var(--ink); color: var(--paper); height: 293px; }

  .holder { position: absolute; left: 24px; top: 35px; }
  .holder-name { font-weight: 700; font-size: 19px; line-height: 21px; }
  .holder-line { font-size: 14px; line-height: 17px; }

  .company { position: absolute; right: 26px; top: 33px; text-align: right; font-size: 14px; line-height: 17.5px; }
  .company-name { font-weight: 700; }

  .wordmark-front {
    position: absolute; left: 0; right: 0; top: 142px; text-align: center;
    font-family: "Roboto", sans-serif; font-weight: 500; font-size: 48px; line-height: 56px; color: var(--ink);
  }
  .wordmark sup { font-size: 10px; font-weight: 400; vertical-align: 34px; margin-left: 2px; }

  .contact-band {
    position: absolute; left: 0; right: 0; top: 241px; height: 35px; background: var(--ink); color: var(--paper);
    display: flex; align-items: center; justify-content: center; font-size: 14px;
  }
  .contact-band .divider { margin: 0 5px; }

  .tagline {
    position: absolute; left: 0; right: 0; top: 39px; text-align: center;
    font-family: "Arimo", Arial, sans-serif; font-weight: 700; font-size: 15.5px; line-height: 19px; letter-spacing: 0.2px;
  }
  .wordmark-back {
    position: absolute; left: 0; right: 0; top: 112px; text-align: center;
    font-family: "Roboto", sans-serif; font-weight: 400; font-size: 62px; line-height: 72px; color: var(--paper);
  }
  .wordmark-back sup { font-size: 10px; vertical-align: 44px; }

  .web-band {
    position: absolute; left: 0; right: 0; top: 238px; height: 35px; background: var(--paper); color: var(--mid);
    display: flex; align-items: center; justify-content: center;
    font-family: "Arimo", Arial, sans-serif; font-weight: 700; font-size: 14px;
  }
</style>
</head>
<body>
  <section class="card card-front" aria-label="Card front">
    <div class="holder">
      <p class="holder-name">Daniel Hale</p>
      <p class="holder-line">Los Angeles Office</p>
      <p class="holder-line">Managing Director</p>
    </div>
    <address class="company" style="font-style:normal">
      <p class="company-name">Stonefield Partners, Inc</p>
      <p>Headquarters 218</p>
      <p>Harbor Lane Suite 40</p>
      <p>Port Ellis, WA 98000</p>
    </address>
    <p class="wordmark wordmark-front">Stonefield<sup>TM</sup></p>
    <div class="contact-band">
      <span>555.014.2273</span><span class="divider">|</span><span>dhale@stonefieldpartners.com</span>
    </div>
  </section>

  <section class="card card-back" aria-label="Card back">
    <p class="tagline">THE PREFERRED CHOICE<br>FOR LEADERSHIP'S TOP PRIORITIES</p>
    <p class="wordmark wordmark-back">Stonefield<sup>TM</sup></p>
    <div class="web-band">www.StonefieldPartners.com</div>
  </section>
</body>
</html>
```